Modern luxury trendy cosmetics label

Looking for a cosmetics packaging label design. We are looking for a professionel, modern and luxury look like Lorena Vasquel, Meadowkin Apothecary, Marigold Tessin, Gavin Albert Pruke, Zuna, Orvik + Dalle, Velumi, Sleepy Walrus, the plainfold, lumiere de sable.Name of product: Nordic Tulip Mask - Needle-Free Contour Ritual Ingredients that have scientific proof of anti aging: Cherry blossom extact, collegen, hyaluronic acid, coconut oil. Color of product itself: Pastel pink. Smell: Cherry blossom. Colors of label: simple and black and white or some subtle colors.

Target Market(s)

Women, luxury market, modern women, young and old women

Industry/Entity Type

Cosmetics

Font styles to use
Sans Serif

Colors

Designer to choose colors to be used in the design.

Requirements
Must have
• A modern look, professional, cosmetics, beauty, professional market, original

```html
<!DOCTYPE html>
<html lang="en">
<head>
<meta charset="utf-8">
<title>Nordic Tulip Mask — Label</title>
<link href="https://fonts.googleapis.com/css2?family=Advent+Pro:wght@200;300&display=swap" rel="stylesheet">
<style>
  :root {
    --backdrop: #2f2133;
    --leaf-plum: #3a2640;
    --leaf-violet: #4b2d5e;
    --leaf-red: #6e1d1f;
    --leaf-deep: #1e1422;
    --panel-white: #ececec;
    --ink: #1a1a1a;
    --brand-ink: #d9d6dc;
    --small-ink: #8a7f8e;
  }
  html, body {
    margin: 0;
    padding: 0;
    width: 1200px;
    height: 1200px;
    overflow: hidden;
    background: var(--backdrop);
  }
  .canvas {
    position: relative;
    width: 1200px;
    height: 1200px;
  }
  .label {
    position: absolute;
    left: 250px;
    top: 220px;
    width: 700px;
    height: 760px;
    overflow: hidden;
  }
  .label__pattern {
    position: absolute;
    inset: 0;
    width: 100%;
    height: 100%;
  }
  .name-panel {
    position: absolute;
    left: 32px;
    top: 196px;
    width: 628px;
    height: 236px;
    box-sizing: border-box;
    background: var(--panel-white);
    border: 2px solid var(--ink);
    display: flex;
    flex-direction: column;
    justify-content: center;
    align-items: center;
  }
  .name-panel__title {
    margin: 0;
    font-family: "Advent Pro", sans-serif;
    font-weight: 200;
    font-size: 70px;
    line-height: 1.05;
    letter-spacing: 0.42em;
    color: var(--ink);
    text-align: center;
    text-transform: lowercase;
  }
  .name-panel__line { display: block; padding-left: 0.42em; }
  .volume {
    position: absolute;
    left: 14px;
    bottom: 78px;
    font-family: "Advent Pro", sans-serif;
    font-weight: 300;
    font-size: 18px;
    letter-spacing: 0.3em;
    color: var(--small-ink);
  }
  .brand {
    position: absolute;
    left: 0;
    right: 0;
    bottom: 48px;
    text-align: center;
    font-family: "Advent Pro", sans-serif;
    font-weight: 300;
    font-size: 50px;
    letter-spacing: 0.02em;
    color: var(--brand-ink);
  }
</style>
</head>
<body>
<main class="canvas">
  <section class="label">
    <svg class="label__pattern" viewBox="0 0 700 760" preserveAspectRatio="none" role="img" aria-label="Pattern of outlined leaves in plum, violet and deep red covering the label">
      <defs>
        <linearGradient id="leafField" x1="0" y1="0" x2="1" y2="1">
          <stop offset="0" stop-color="var(--leaf-violet)"/>
          <stop offset="0.35" stop-color="var(--leaf-plum)"/>
          <stop offset="0.6" stop-color="var(--leaf-red)"/>
          <stop offset="1" stop-color="var(--leaf-deep)"/>
        </linearGradient>
      </defs>
      <rect width="700" height="760" fill="url(#leafField)"/>
    </svg>

    <div class="name-panel">
      <h1 class="name-panel__title">
        <span class="name-panel__line">nordic</span>
        <span class="name-panel__line">tulip mask</span>
      </h1>
    </div>

    <div class="volume">200 ml</div>
    <div class="brand">aveln</div>
  </section>
</main>
</body>
</html>
```